Business Card for Pottery and Jewellery Designer

A new business card design is needed to accompany a newly launching pottery and jewellery website. The company logo has been attached for use. The company is called Kilnwick Lane. For a sense of the vibe please see the website (it is currently under construction but this way you'll get a feel for the style) www.KilnwickLane.com

The website font is Pontano Sans for the body of the text with Overlock for headers.

The overall look should be clean and elegant. The back side can have just the logo. The front side should have a smaller logo and the following details displayed:

Kilnwick Lane
Designer: Marisol Bexley
Phone: xxx.xxx.xxxx
Email: Designer@KilnwickLane.com

The structure of displaying this is completely up to you. Different layouts and creative methods of displaying contact info are welcome as long as it stays clean/uncluttered.

No product photographs are to be included in the design as the catalogue changes quickly.

Colour preferences lean towards elegant and understated (charcoal grey, dark navy blue etc.)

Please let me know if you have any further questions or further details required.

Target Market(s)

Target market is 30+ year old women

Industry/Entity Type

Construction

Colors
ffffff
1b1b1b
474747
d9d9d9
fafafa
0355a3

Requirements
Must have
• The submissions so far have looked very typical and don't stand out right now. They're also all in navy with very little variation. I'm looking for something that stands out a it more while still being clean-looking.
Nice to have
• I've attached a few design samples and an idea for a backdrop. It would be great to see some designs in black, white, and grey with only a hint of color.
Should not have
• Product Images

```html
<!DOCTYPE html>
<html lang="en">
<head>
<meta charset="utf-8">
<title>Kilnwick Lane — Business Card</title>
<link rel="stylesheet" href="https://fonts.googleapis.com/css2?family=Overlock:wght@400;700&family=Pontano+Sans&display=swap">
<style>
  :root {
    --backdrop: #6b3a26;
    --card-dark: #1b1b1b;
    --card-dark-glow: #242424;
    --card-light: #fafafa;
    --card-light-edge: #e6e6e6;
    --ink-light: #ffffff;
    --ink-dark: #1b1b1b;
    --ink-mid: #2a2a2a;
    --mark-grey: #d9d9d9;
    --mark-dark: #474747;
  }
  * { box-sizing: border-box; margin: 0; padding: 0; }
  html, body {
    width: 1200px;
    height: 1181px;
    overflow: hidden;
  }
  body {
    position: relative;
    background: var(--backdrop);
    font-family: "Pontano Sans", sans-serif;
  }
  .card {
    position: absolute;
    left: 230px;
    width: 740px;
    height: 426px;
    box-shadow: 0 3px 10px rgba(0, 0, 0, 0.45);
  }
  .card-back {
    top: 110px;
    background: radial-gradient(ellipse at 50% 50%, var(--card-dark-glow) 0%, var(--card-dark) 70%);
  }
  .card-front {
    top: 635px;
    background: radial-gradient(ellipse at 50% 45%, #ffffff 0%, var(--card-light) 45%, var(--card-light-edge) 100%);
  }
  .brand-lockup {
    position: absolute;
    left: 152px;
    top: 198px;
    display: flex;
    align-items: center;
    gap: 18px;
  }
  .brand-dot {
    width: 30px;
    height: 30px;
    border-radius: 50%;
    background: var(--mark-grey);
  }
  .brand-name {
    font-family: "Overlock", sans-serif;
    font-weight: 400;
    font-size: 31px;
    letter-spacing: 0.3px;
    text-transform: uppercase;
    color: var(--ink-light);
    line-height: 1;
  }
  .front-brand {
    position: absolute;
    left: 160px;
    top: 168px;
    width: 150px;
    font-family: "Overlock", sans-serif;
    font-weight: 700;
    font-size: 30px;
    line-height: 1.05;
    color: var(--mark-dark);
  }
  .contact {
    position: absolute;
    left: 334px;
    top: 170px;
  }
  .contact-name {
    font-family: "Overlock", sans-serif;
    font-weight: 700;
    font-size: 27px;
    color: var(--ink-dark);
    line-height: 1;
    margin-bottom: 14px;
  }
  .contact-line {
    font-size: 16.5px;
    color: var(--ink-mid);
    line-height: 27px;
  }
</style>
</head>
<body>
  <section class="card card-back">
    <div class="brand-lockup">
      <span class="brand-dot"></span>
      <span class="brand-name">Kilnwick Lane</span>
    </div>
  </section>

  <section class="card card-front">
    <div class="front-brand">Kilnwick Lane</div>
    <div class="contact">
      <p class="contact-name">Marisol Bexley</p>
      <p class="contact-line">Designer@KilnwickLane.com</p>
      <p class="contact-line">123-456-7890</p>
    </div>
  </section>
</body>
</html>
```